Test and Tag business card design

We are an appliance test and tag company in Brisbane Australia requiring a business card design.
I don't have a logo.
Card front: Matte black background with white font.
Card back: White background with black font colour
Examples are attached
Minimalist design
Reason: Looking for more designs with an extreme minimal feel
Industry/Entity Type
Appliance
Contact Information for Business Card
Business name: Harbor Check and Label
Description: Onsite Electrical Testing and Tagging
Licence No. 41853
Name: Greg Pellow
Mobile: 0418 526 937
Email: greg@harborcheckandlabel.com.au
Web: harborcheckandlabel.com.au
Logo Text
Harbor Check and Label
Look and feel

```html
<!DOCTYPE html>
<html lang="en">
<head>
<meta charset="utf-8">
<title>Harbor Check and Label – Business Card</title>
<link rel="stylesheet" href="https://fonts.googleapis.com/css2?family=Fira+Sans:wght@400;600&display=swap">
<style>
  :root {
    --stage: #dfe2e6;
    --card-black: #1b1b1b;
    --card-white: #f2f3f3;
    --ink-light: #f4f4f4;
    --ink-muted: #bdbdbd;
    --ink-dark: #2a2a2a;
    --ink-grey: #7a7a7a;
    --divider: #d8d8d8;
  }
  * { box-sizing: border-box; margin: 0; padding: 0; }
  html, body {
    width: 1200px;
    height: 900px;
    overflow: hidden;
    background: var(--stage);
    font-family: "Fira Sans", Arial, sans-serif;
  }
  .stage {
    position: relative;
    width: 1200px;
    height: 900px;
  }
  .card {
    position: absolute;
    top: 300px;
    width: 525px;
    height: 300px;
    box-shadow: 0 10px 24px rgba(0, 0, 0, 0.12);
  }

  /* Front: black */
  .card--front {
    left: 40px;
    background: var(--card-black);
    color: var(--ink-light);
  }
  .brand-column {
    position: absolute;
    left: 26px;
    top: 0;
    height: 300px;
    padding: 28px 0;
    writing-mode: vertical-rl;
    transform: rotate(180deg);
    display: flex;
    flex-direction: column;
    gap: 8px;
  }
  .brand-column .brand-name {
    font-weight: 600;
    font-size: 24px;
    letter-spacing: 0.2px;
    color: var(--ink-light);
  }
  .brand-column .brand-line {
    font-weight: 400;
    font-size: 13px;
    color: var(--ink-muted);
    letter-spacing: 0.3px;
  }
  .divider {
    position: absolute;
    left: 170px;
    top: 40px;
    width: 2px;
    height: 220px;
    background: linear-gradient(to bottom, rgba(216,216,216,0) 0%, var(--divider) 40%, var(--divider) 60%, rgba(216,216,216,0) 100%);
  }
  .contact {
    position: absolute;
    left: 210px;
    top: 62px;
  }
  .contact .person {
    font-weight: 600;
    font-size: 27px;
    margin-bottom: 26px;
  }
  .contact ul { list-style: none; }
  .contact li {
    display: flex;
    align-items: center;
    gap: 12px;
    font-size: 15px;
    letter-spacing: 0.3px;
    margin-bottom: 15px;
  }
  .contact svg {
    width: 15px;
    height: 15px;
    flex: none;
    fill: none;
    stroke: var(--ink-light);
    stroke-width: 1.8;
  }

  /* Back: white */
  .card--back {
    left: 635px;
    background: var(--card-white);
    color: var(--ink-dark);
    display: flex;
    flex-direction: column;
    align-items: center;
    justify-content: center;
    gap: 10px;
  }
  .card--back .brand-name {
    font-weight: 600;
    font-size: 26px;
    letter-spacing: 0.2px;
  }
  .card--back .brand-web {
    font-size: 14px;
    color: var(--ink-grey);
    letter-spacing: 0.5px;
  }
</style>
</head>
<body>
<main class="stage">
  <section class="card card--front" aria-label="Business card front">
    <div class="brand-column">
      <span class="brand-name">Harbor Check and Label</span>
      <span class="brand-line">Onsite Electrical Testing &amp; Tagging</span>
      <span class="brand-line">Licence No. 41853</span>
    </div>
    <div class="divider"></div>
    <div class="contact">
      <h1 class="person">Greg Pellow</h1>
      <ul>
        <li>
          <svg viewBox="0 0 16 16" aria-hidden="true"><path d="M4 2 L6 5 L5 6.5 C6 8.5 7.5 10 9.5 11 L11 10 L14 12 L12.5 14 C7 13.5 2.5 9 2 3.5 Z"/></svg>
          0418 526 937
        </li>
        <li>
          <svg viewBox="0 0 16 16" aria-hidden="true"><rect x="1.5" y="3.5" width="13" height="9"/><path d="M1.5 3.5 L8 9 L14.5 3.5"/></svg>
          greg@harborcheckandlabel.com.au
        </li>
        <li>
          <svg viewBox="0 0 16 16" aria-hidden="true"><circle cx="9.5" cy="6.5" r="4"/><path d="M6.6 9.4 L2 14"/></svg>
          www.harborcheckandlabel.com.au
        </li>
      </ul>
    </div>
  </section>

  <section class="card card--back" aria-label="Business card back">
    <span class="brand-name">Harbor Check and Label</span>
    <span class="brand-web">www.harborcheckandlabel.com.au</span>
  </section>
</main>
</body>
</html>
```